business cards, stationary, envelopes,
Brindle Houses business cards
business cards, stationary, envelopes,  - Construction
Creative Brief
Professional
Dale R. Morrow
President
412 NE State Route 19 #208 Larkfield, MO 64990
dale@brindlehousesmk.example
www.brindlehousesmk.example

```html
<!DOCTYPE html>
<html lang="en">
<head>
<meta charset="utf-8">
<title>Brindle Houses business cards</title>
<link rel="stylesheet" href="https://fonts.googleapis.com/css2?family=Jost:wght@400;500;600&display=swap">
<style>
  :root {
    --backdrop: #e8e3dc;
    --card-white: #ffffff;
    --brand-red: #d9161f;
    --brand-red-deep: #a80f17;
    --brand-red-dark: #8e0c13;
    --text-gray: #555555;
    --text-dark: #333333;
    --gold: #b8872c;
  }
  * { box-sizing: border-box; margin: 0; padding: 0; }
  html, body { width: 1200px; height: 826px; overflow: hidden; }
  body {
    background: var(--backdrop);
    font-family: "Jost", Arial, sans-serif;
    position: relative;
  }
  .card {
    position: absolute;
    width: 516px;
    height: 264px;
    border-radius: 20px;
    overflow: hidden;
    box-shadow: 0 4px 12px rgba(0,0,0,0.18);
  }
  .card-front { left: 84px; top: 108px; background: var(--card-white); }
  .card-back-red-band { left: 636px; top: 108px; background: linear-gradient(90deg, var(--brand-red) 0%, var(--brand-red-deep) 100%); }
  .card-back-white { left: 84px; top: 456px; background: var(--card-white); }
  .card-back-red { left: 636px; top: 456px; background: radial-gradient(ellipse at 50% 45%, var(--brand-red) 0%, var(--brand-red-dark) 100%); }

  .wordmark {
    position: absolute;
    left: 0; right: 0;
    text-align: center;
    font-weight: 500;
    letter-spacing: 3px;
    text-transform: uppercase;
    line-height: 1;
  }
  .wordmark-front { top: 46px; font-size: 36px; color: var(--gold); }
  .wordmark-red { top: 104px; font-size: 30px; color: var(--brand-red); }
  .wordmark-white { font-size: 30px; color: #ffffff; }
  .card-back-red-band .wordmark-white { top: 100px; }
  .card-back-red .wordmark-white { top: 104px; }

  .contact {
    position: absolute;
    left: 0; right: 0;
    top: 96px;
    text-align: center;
    color: var(--text-gray);
    font-size: 12.5px;
    line-height: 18px;
  }
  .contact .label { color: var(--brand-red); font-weight: 500; }
  .contact .website {
    margin-top: 2px;
    font-size: 14px;
    font-weight: 600;
    letter-spacing: 3px;
    color: var(--text-dark);
  }

  .name-band { position: absolute; left: 0; bottom: 0; width: 516px; height: 64px; }
  .holder {
    position: absolute;
    left: 0; right: 0;
    bottom: 10px;
    text-align: center;
    color: #ffffff;
    line-height: 16px;
  }
  .holder-name { font-size: 14px; }
  .holder-title { font-size: 11px; }

  .url {
    position: absolute;
    left: 0; right: 0;
    text-align: center;
    font-size: 14px;
    letter-spacing: 0.5px;
  }
  .url-on-white-band { bottom: 14px; color: var(--text-gray); }
  .url-gray { top: 150px; color: var(--text-dark); }
  .url-white { top: 160px; color: #ffffff; }

  .white-band { position: absolute; left: 0; bottom: 0; width: 516px; height: 70px; }
</style>
</head>
<body>

  <section class="card card-front" aria-label="Business card front">
    <div class="wordmark wordmark-front">Brindle Houses</div>
    <div class="contact">
      <p>412 NE State Route 19 #208, Larkfield, MO 64990</p>
      <p><span class="label">P:</span> 816-555-0142 &nbsp;•&nbsp; <span class="label">C:</span> 816-555-0187 &nbsp;•&nbsp; <span class="label">F:</span> 816-555-0163</p>
      <p><span class="label">E:</span> dale@brindlehousesmk.example</p>
      <p class="website">www.brindlehousesmk.example</p>
    </div>
    <svg class="name-band" viewBox="0 0 516 64" preserveAspectRatio="none" aria-hidden="true">
      <polygon points="0,30 258,0 516,30 516,64 0,64" fill="var(--brand-red)"/>
    </svg>
    <div class="holder">
      <p class="holder-name">Dale R. Morrow</p>
      <p class="holder-title">President</p>
    </div>
  </section>

  <section class="card card-back-red-band" aria-label="Business card back, red with white band">
    <div class="wordmark wordmark-white">Brindle Houses</div>
    <svg class="white-band" viewBox="0 0 516 70" preserveAspectRatio="none" aria-hidden="true">
      <polygon points="0,38 258,0 516,38 516,70 0,70" fill="var(--card-white)"/>
    </svg>
    <div class="url url-on-white-band">www.brindlehousesmk.example</div>
  </section>

  <section class="card card-back-white" aria-label="Business card back, white">
    <div class="wordmark wordmark-red">Brindle Houses</div>
    <div class="url url-gray">www.brindlehousesmk.example</div>
  </section>

  <section class="card card-back-red" aria-label="Business card back, red">
    <div class="wordmark wordmark-white">Brindle Houses</div>
    <div class="url url-white">www.brindlehousesmk.example</div>
  </section>

</body>
</html>
```